DJ Kovan Threl

I'm looking for a professional but still artsy/progressive design. I come from a hip hop/club DJ background playing a lot of underground music but have switched to doing more corporate parties and weddings recently. I am all about keeping the dancefloor moving and emotionally connecting with the crowd. I'd like a trendy/updated color palette. Something that's clean enough that looks professional but also trendy enough to convey that by the end of the night we'll be sweatily dancing to the latest hits. Some designers/artists I like: Rolo Partague, Wendel Ashby, Tobiah Crane, Vexmor 3100, Lyle Brandish.

```html
<!DOCTYPE html>
<html lang="en">
<head>
<meta charset="UTF-8">
<title>DJ Kovan Threl – Business Card</title>
<link href="https://fonts.googleapis.com/css2?family=Roboto+Condensed:wght@700&family=Roboto:wght@400;700&display=swap" rel="stylesheet">
<style>
  :root {
    --backdrop: #2a2a2c;
    --card: #170d12;
    --title: #ffe500;
    --contact: #ffffff;
    --splash-blue: #2a2fb8;
    --splash-red: #a8241c;
    --splash-yellow: #e8c61e;
    --splash-white: #dfe3ee;
  }
  * { margin: 0; padding: 0; box-sizing: border-box; }
  html, body {
    width: 1200px;
    height: 1200px;
    overflow: hidden;
    background: var(--backdrop);
  }
  .business-card {
    position: absolute;
    left: 50px;
    top: 286px;
    width: 1100px;
    height: 628px;
    background: var(--card);
    overflow: hidden;
  }
  .paint-splash {
    position: absolute;
    left: 470px;
    top: 0;
    width: 630px;
    height: 628px;
    background:
      linear-gradient(90deg, var(--card) 0%, rgba(23,13,18,0) 22%),
      linear-gradient(160deg, var(--splash-blue) 0%, var(--splash-red) 38%, var(--splash-yellow) 58%, var(--splash-white) 78%, var(--splash-blue) 100%);
    opacity: 0.85;
  }
  .dj-name {
    position: absolute;
    left: 92px;
    top: 76px;
    font-family: "Roboto Condensed", sans-serif;
    font-weight: 700;
    font-size: 68px;
    line-height: 1.0;
    color: var(--title);
    letter-spacing: -0.5px;
  }
  .contact {
    position: absolute;
    left: 92px;
    top: 392px;
    font-family: "Roboto", sans-serif;
    color: var(--contact);
    list-style: none;
  }
  .contact li { font-size: 30px; line-height: 1.24; }
  .contact .phone { font-weight: 700; font-size: 33px; letter-spacing: 1px; }
</style>
</head>
<body>
  <section class="business-card">
    <div class="paint-splash" role="img" aria-label="Abstract explosive paint splatter in yellow, red, blue and white streaks"></div>
    <h1 class="dj-name">DJ<br>KOVAN THREL</h1>
    <ul class="contact">
      <li class="phone">0972 418 650</li>
      <li class="email">KovanThrel@mailbox.net</li>
      <li class="web">www.djkovanthrel.net</li>
    </ul>
  </section>
</body>
</html>
```